New Business Card Design Project

We are a spa looking to create a professional elegant business card for a spa mainly black and white with a splash of lime green. This card will be two sided - the front side will have an image, the logo, and the spa's information - the back side will have a promotion for new customers - NEW CUSTOMERS $20 OFF

Look and feel: chic, modern, and spa-ish.
Information to be included:
Therapist Name
Therapist specialty
Address: 5147 Marlowe Ave, Beverly Hills CA 90211
Phone: (310) 482-3961

Let me know if you have any questions!

Thank you

```html
<!DOCTYPE html>
<html lang="en">
<head>
<meta charset="utf-8">
<title>Verra Day Spa – Business Card</title>
<link href="https://fonts.googleapis.com/css2?family=Cinzel:wght@400;600&family=Open+Sans:wght@400;700&display=swap" rel="stylesheet">
<style>
  :root {
    --page-bg: #efefec;
    --lime-light: #c6ea6a;
    --lime: #9fd43a;
    --lime-deep: #7fb91f;
    --ink: #1c1c1c;
    --portrait-tone-a: #dfe6ec;
    --portrait-tone-b: #c9b8ad;
    --stone-tone-a: #e9eef2;
    --stone-tone-b: #4a5358;
    --card-shadow: rgba(0,0,0,0.18);
  }
  * { box-sizing: border-box; margin: 0; padding: 0; }
  html, body {
    width: 1200px; height: 1023px; overflow: hidden;
    background: var(--page-bg);
  }
  .card {
    position: absolute; left: 250px; width: 700px; height: 400px;
    border-radius: 6px; overflow: hidden;
    background: linear-gradient(135deg, var(--lime-light), var(--lime) 55%, var(--lime-deep));
    box-shadow: 0 10px 28px var(--card-shadow);
  }
  .card--front { top: 78px; }
  .card--back { top: 545px; }
  .card-art { position: absolute; inset: 0; width: 700px; height: 400px; }

  .brand {
    position: absolute; display: flex; align-items: center; justify-content: center;
    flex-direction: column; border: 4px solid var(--ink); border-radius: 50%;
    font-family: "Cinzel", serif; font-weight: 600; color: var(--ink);
    text-align: center; line-height: 1.15; letter-spacing: 2px;
  }
  .card--front .brand { left: 150px; top: 28px; width: 150px; height: 150px; font-size: 19px; }
  .card--back .brand { left: 60px; top: 80px; width: 240px; height: 240px; font-size: 30px; }

  .therapist {
    position: absolute; left: 360px; top: 190px; color: var(--ink);
    font-family: "Open Sans", sans-serif;
  }
  .therapist__name { font-family: "Cinzel", serif; font-size: 26px; font-weight: 400; letter-spacing: 1px; }
  .therapist__specialty { font-size: 12px; letter-spacing: 1px; margin-bottom: 14px; }
  .therapist__phone, .therapist__address { font-size: 15px; line-height: 1.5; }
  .therapist__phone { margin-bottom: 10px; }

  .promo {
    position: absolute; left: 335px; top: 135px; width: 345px;
    color: var(--ink); text-align: center; white-space: nowrap;
  }
  .promo__label { font-family: "Cinzel", serif; font-size: 30px; line-height: 1.2; letter-spacing: 1px; }
  .promo__offer { font-family: "Open Sans", sans-serif; font-weight: 700; font-size: 72px; line-height: 1.1; }
</style>
</head>
<body>
  <section class="card card--front">
    <svg class="card-art" viewBox="0 0 700 400">
      <defs>
        <linearGradient id="stoneTones" x1="0" y1="0" x2="1" y2="1">
          <stop offset="0" stop-color="#e9eef2"/>
          <stop offset="1" stop-color="#4a5358"/>
        </linearGradient>
        <linearGradient id="portraitTones" x1="0" y1="0" x2="1" y2="0">
          <stop offset="0" stop-color="#c9b8ad"/>
          <stop offset="1" stop-color="#dfe6ec"/>
        </linearGradient>
      </defs>
      <path role="img" aria-label="Photo of stacked black spa stones with blue flowers"
            d="M360 0 H700 V175 C610 160 470 110 360 0 Z" fill="url(#stoneTones)"/>
      <path role="img" aria-label="Photo of a relaxed woman resting on white towels"
            d="M0 200 C130 205 250 250 340 400 H0 Z" fill="url(#portraitTones)"/>
    </svg>
    <div class="brand">Verra<br>Day Spa</div>
    <div class="therapist">
      <p class="therapist__name">Dana Whitfield</p>
      <p class="therapist__specialty">THERAPIST SPECIALTY</p>
      <p class="therapist__phone">(310) 482-3961</p>
      <p class="therapist__address">5147 Marlowe Ave<br>Beverly Hills CA 90211</p>
    </div>
  </section>

  <section class="card card--back">
    <div class="brand">Verra<br>Day Spa</div>
    <div class="promo">
      <p class="promo__label">NEW CUSTOMERS</p>
      <p class="promo__offer">$20 OFF</p>
    </div>
  </section>
</body>
</html>
```